Dean harlowe realestate

We want something complete different to our website now and something that will stand out this is our website http://deanharlowerealestate-demo.com/

our company website for my boss is www.stevenorrick-demo.com

please note this website is being made for dean harlowe not steven orrick

something similar to our company website but has to be in the branding of dean harlowe realestate

```html
<!DOCTYPE html>
<html lang="en">
<head>
<meta charset="utf-8">
<title>Dean Harlowe Property</title>
<link rel="stylesheet" href="https://fonts.googleapis.com/css2?family=Poppins:wght@400;500;600;700&family=Roboto:wght@400;500;700&display=swap">
<style>
  :root {
    --ink: #111111;
    --brand-blue: #1f6fb4;
    --accent-blue: #2e96dc;
    --button-blue: #3497db;
    --price-green: #35c31c;
    --arrow-cyan: #16d9d6;
    --panel: #f5f5f5;
    --field-border: #cfcfcf;
    --track-grey: #a9a9a9;
    --white: #ffffff;
    --caption-bg: rgba(40, 40, 40, 0.72);
    --hero-light: #d9dcdf;
    --hero-dark: #8d9196;
  }
  * { box-sizing: border-box; margin: 0; padding: 0; }
  html, body { width: 1200px; height: 1040px; overflow: hidden; background: var(--white); }
  body { font-family: "Poppins", sans-serif; color: var(--ink); position: relative; }

  .site-header { position: absolute; left: 0; top: 0; width: 1200px; height: 113px; }
  .brand { position: absolute; left: 32px; top: 30px; display: flex; align-items: center; gap: 12px; }
  .brand-mark { width: 44px; height: 44px; background: var(--brand-blue); }
  .brand-name { font-family: "Poppins", sans-serif; font-weight: 600; font-size: 25px; line-height: 1.05; color: var(--brand-blue); text-transform: uppercase; letter-spacing: 0.5px; }
  .main-nav { position: absolute; right: 60px; top: 52px; display: flex; gap: 15px; }
  .main-nav a { font-size: 17px; font-weight: 500; color: var(--ink); text-decoration: none; letter-spacing: 0.6px; }

  .hero { position: absolute; left: 0; top: 113px; width: 1200px; height: 605px; }
  .hero-photo { position: absolute; inset: 0;
    background: linear-gradient(180deg, var(--hero-light) 0%, var(--hero-dark) 100%); }
  .listing-bar { position: absolute; left: 24px; top: 539px; height: 66px; width: 1128px; display: flex; }
  .listing-address { flex: 0 0 709px; background: var(--caption-bg); color: var(--white); font-size: 15px; letter-spacing: 0.4px; text-transform: uppercase; display: flex; align-items: center; padding-left: 24px; }
  .listing-details { flex: 0 0 120px; background: var(--accent-blue); color: var(--white); font-size: 15px; display: flex; align-items: center; justify-content: center; gap: 12px; }
  .listing-price { flex: 0 0 184px; background: var(--price-green); color: var(--white); font-size: 20px; font-weight: 600; display: flex; align-items: center; justify-content: center; }
  .listing-arrow { flex: 0 0 57px; background: var(--arrow-cyan); display: flex; align-items: center; justify-content: center; border-left: 1px solid rgba(0,0,0,0.15); }

  .search-panel { position: absolute; left: 0; top: 718px; width: 1200px; height: 280px; background: var(--panel); font-family: "Roboto", sans-serif; }
  .field { position: absolute; top: 52px; width: 247px; }
  .field-label { font-size: 14px; font-weight: 700; color: var(--ink); margin-bottom: 16px; }
  .field-select { height: 37px; background: var(--white); border: 1px solid var(--field-border); display: flex; align-items: center; justify-content: space-between; padding-left: 16px; font-size: 13px; color: #777; }
  .select-caret { width: 18px; height: 33px; border-left: 1px solid var(--field-border); background: #ececec; display: flex; align-items: center; justify-content: center; margin-right: 1px; }

  .price-label { position: absolute; left: 53px; top: 157px; font-size: 14px; font-weight: 700; }
  .price-track { position: absolute; left: 53px; top: 190px; width: 525px; height: 10px; background: var(--button-blue); }
  .price-track .selected { position: absolute; left: 104px; width: 210px; top: 0; height: 10px; background: var(--track-grey); }
  .handle { position: absolute; top: -4px; width: 17px; height: 17px; background: var(--white); border: 2px solid var(--button-blue); }
  .price-value { position: absolute; left: 607px; top: 178px; font-family: "Poppins", sans-serif; font-size: 23px; font-weight: 600; color: var(--accent-blue); }
  .search-button { position: absolute; left: 879px; top: 163px; width: 253px; height: 49px; background: var(--button-blue); border: 1px solid #2a86c4; color: var(--white); font-size: 16px; font-weight: 700; display: flex; align-items: center; justify-content: center; letter-spacing: 0.5px; }
</style>
</head>
<body>
  <header class="site-header">
    <div class="brand">
      <span class="brand-mark"></span>
      <span class="brand-name">Dean Harlowe<br>Property</span>
    </div>
    <nav class="main-nav">
      <a href="#">HOME</a><a href="#">ABOUT</a><a href="#">FOR SALE</a><a href="#">AGENTS</a><a href="#">BOOK APPRAISAL</a><a href="#">CONTACT</a>
    </nav>
  </header>

  <section class="hero">
    <div class="hero-photo" role="img" aria-label="Photo of a bright modern living room with sofa, armchairs, fireplace and a glass wall opening onto a garden"></div>
    <div class="listing-bar">
      <div class="listing-address">2/18 Harbour Crest Avenue, Kellmont Bay, NSW 2090</div>
      <div class="listing-details">
        <svg width="18" height="18" viewBox="0 0 18 18"><path d="M1 1h16v10l-6 6H1z" fill="#fff"/><path d="M11 17v-6h6" fill="#cfe6f6"/></svg>
        Details
      </div>
      <div class="listing-price">$359,000.00</div>
      <div class="listing-arrow"><svg width="12" height="16" viewBox="0 0 12 16"><path d="M9 2 3 8l6 6" stroke="#fff" stroke-width="3" fill="none"/></svg></div>
      <div class="listing-arrow"><svg width="12" height="16" viewBox="0 0 12 16"><path d="M3 2l6 6-6 6" stroke="#fff" stroke-width="3" fill="none"/></svg></div>
    </div>
  </section>

  <section class="search-panel">
    <div class="field" style="left:53px"><div class="field-label">Min Of Bedrooms</div><div class="field-select">Any<span class="select-caret"><svg width="8" height="5" viewBox="0 0 8 5"><path d="M0 0h8L4 5z" fill="#666"/></svg></span></div></div>
    <div class="field" style="left:330px"><div class="field-label">Min Of Bathrooms</div><div class="field-select">Any<span class="select-caret"><svg width="8" height="5" viewBox="0 0 8 5"><path d="M0 0h8L4 5z" fill="#666"/></svg></span></div></div>
    <div class="field" style="left:607px"><div class="field-label">Min Area(Sqft)</div><div class="field-select">Any<span class="select-caret"><svg width="8" height="5" viewBox="0 0 8 5"><path d="M0 0h8L4 5z" fill="#666"/></svg></span></div></div>
    <div class="field" style="left:884px"><div class="field-label">Max Area(Sqft)</div><div class="field-select">Any<span class="select-caret"><svg width="8" height="5" viewBox="0 0 8 5"><path d="M0 0h8L4 5z" fill="#666"/></svg></span></div></div>

    <div class="price-label">Pricing Range</div>
    <div class="price-track">
      <span class="selected"></span>
      <span class="handle" style="left:96px"></span>
      <span class="handle" style="left:306px"></span>
    </div>
    <div class="price-value">$10000 - $30000</div>
    <div class="search-button">SEARCH</div>
  </section>
</body>
</html>
```